Business Cards Design for the electrical wholesaler: clean bold dynamic :)

We need a business card design that would follow our latest brand guidelines. As an electrical wholesaler we want to bring a fresh look and feel into the industry. The design should be clean bold and dynamic. It should come alive with the renewed energy of our green colour. Our grey colour should keep things balanced and complement the notion of maturity and responsibility. We employ Lato as a corporate font however are not bound by this font and we’re open to interpretation here.

Target Market(s)

Electrical contractors

Industry/Entity Type

Business

Contact Information for Business Card

Logo
Name & Surname: Olena Dovbush
Job Title: Director of Marketing
Email: helen.dovbush@mailvane.example
Cell phone: XXX.XXX.XXXX
Address: 20917 - 87 Ave. Edmonton, AB, Canada. T6K 2R8
Business Phone: 780.555.0187
Website: www.qorvil.example

Font styles to use
Other font styles liked:
• Lato

Requirements
Must have
• Logo & website
Nice to have
• Brand elements - some of them you may find in the attached Brand Guidelines (e.g. three lines on the background signifying "W")

```html
<!DOCTYPE html>
<html lang="en">
<head>
<meta charset="utf-8">
<title>Qorvil Business Card</title>
<link href="https://fonts.googleapis.com/css2?family=Lato:wght@400;700;900&display=swap" rel="stylesheet">
<style>
  :root {
    --brand-green: #8dc63f;
    --brand-grey: #505253;
    --text-dark: #3a3b3c;
    --text-body: #444546;
    --card-white: #ffffff;
    --page-bg: #ffffff;
    --card-shadow: 0 14px 22px rgba(0, 0, 0, 0.38);
  }
  * { margin: 0; padding: 0; box-sizing: border-box; }
  html, body {
    width: 924px;
    height: 1200px;
    overflow: hidden;
    background: var(--page-bg);
    font-family: "Lato", Arial, sans-serif;
  }
  .canvas { position: relative; width: 924px; height: 1200px; }

  .card {
    position: absolute;
    left: 88px;
    width: 744px;
    box-shadow: var(--card-shadow);
  }

  /* Front */
  .card-front {
    top: 92px;
    height: 447px;
    background: var(--brand-green);
    display: flex;
    align-items: center;
    justify-content: center;
  }
  .brand-lockup {
    display: flex;
    align-items: center;
    gap: 16px;
    font-weight: 700;
    letter-spacing: 0.5px;
  }
  .brand-lockup .brand-square {
    width: 46px;
    height: 46px;
  }
  .card-front .brand-lockup { color: var(--card-white); font-size: 74px; }
  .card-front .brand-square { background: var(--card-white); width: 54px; height: 54px; }

  /* Back */
  .card-back {
    top: 627px;
    height: 443px;
    background: var(--card-white);
  }
  .holder-name {
    position: absolute;
    left: 43px;
    top: 64px;
    font-size: 40px;
    font-weight: 700;
    color: var(--brand-green);
  }
  .holder-title {
    position: absolute;
    left: 44px;
    top: 122px;
    font-size: 20px;
    font-weight: 700;
    color: var(--text-dark);
  }
  .card-back .brand-lockup {
    position: absolute;
    left: 384px;
    top: 72px;
    color: var(--brand-grey);
    font-size: 62px;
  }
  .card-back .brand-square { background: var(--brand-green); }

  .contact {
    position: absolute;
    left: 44px;
    color: var(--text-body);
    white-space: nowrap;
  }
  .contact-email { top: 196px; font-size: 17px; }
  .contact-address { top: 224px; font-size: 15px; }
  .contact-phone { top: 288px; font-size: 15px; }
  .contact-business { top: 313px; font-size: 15px; }
  .contact-business strong { font-weight: 700; color: var(--text-dark); }

  .footer-band {
    position: absolute;
    left: 0;
    right: 0;
    bottom: 0;
    height: 49px;
    display: flex;
  }
  .footer-band .band-green { width: 363px; background: var(--brand-green); }
  .footer-band .band-grey {
    flex: 1;
    background: var(--brand-grey);
    color: var(--card-white);
    font-size: 22px;
    display: flex;
    align-items: center;
    justify-content: flex-end;
    padding-right: 38px;
  }
</style>
</head>
<body>
<main class="canvas">
  <section class="card card-front" aria-label="Business card front">
    <div class="brand-lockup">
      <span class="brand-square"></span>
      <span class="brand-name">qorvil</span>
    </div>
  </section>

  <section class="card card-back" aria-label="Business card back">
    <h1 class="holder-name">Olena Dovbush</h1>
    <p class="holder-title">Director of Marketing</p>

    <div class="brand-lockup">
      <span class="brand-square"></span>
      <span class="brand-name">qorvil</span>
    </div>

    <p class="contact contact-email">Email: helen.dovbush@mailvane.example</p>
    <p class="contact contact-address">Address: 20917 - 87 Ave. Edmonton, AB, Canada. T6K 2R8</p>
    <p class="contact contact-phone">Phone: XXX.XXX.XXXX</p>
    <p class="contact contact-business">Business Phone: <strong>780.555.0187</strong></p>

    <div class="footer-band">
      <div class="band-green"></div>
      <div class="band-grey">Website: www.qorvil.example</div>
    </div>
  </section>
</main>
</body>
</html>
```